DRM Letterhead Design Project

Design a new company letterhead utilizing our new logo and color scheme. Interested in professional letterhead and matching 2nd sheet versions.
Updates

I have uploaded windows format files now.  Originally only uploaded MAC file format.  Good luck!

Target Market(s)

Industry Executives, construction managers, well educated and discriminate personnel. Project needs to leave an impression and have impact but not be cluttered, busy or too in your face.

Industry/Entity Type

It Company

Requirements
Must have
• Clean, crisp look, true to new logo and color scheme, professional image. Should include spaces for company web address, address info and phone & fax numbers

```html
<!DOCTYPE html>
<html lang="en">
<head>
<meta charset="utf-8">
<title>DRM Systems Letterhead</title>
<link rel="stylesheet" href="https://fonts.googleapis.com/css2?family=Open+Sans:wght@400;600;700&display=swap">
<style>
  :root {
    --backdrop: #e9e6e1;
    --paper: #ffffff;
    --ink: #1f1f1f;
    --ink-soft: #3a3a3a;
    --brand-orange: #e07f22;
    --brand-grey: #4a4a4c;
    --watermark: #ececec;
    --signature-tone: #d9d9d9;
  }
  * { margin: 0; padding: 0; box-sizing: border-box; }
  html, body {
    width: 1200px; height: 1071px; overflow: hidden;
    background: var(--backdrop);
    font-family: "Open Sans", Arial, sans-serif;
    color: var(--ink);
  }
  .letterhead {
    position: absolute; left: 233px; top: 48px;
    width: 685px; height: 969px;
    background: var(--paper);
    box-shadow: 0 2px 6px rgba(0,0,0,0.25);
    overflow: hidden;
  }
  .brand {
    position: absolute; left: 0; right: 0; top: 50px;
    display: flex; flex-direction: column; align-items: center;
  }
  .brand-dot {
    width: 92px; height: 92px; border-radius: 50%;
    background: var(--brand-grey);
  }
  .brand-name {
    margin-top: 18px;
    font-weight: 700; font-size: 34px; letter-spacing: 3px;
    color: var(--brand-orange); line-height: 1;
  }
  .watermark {
    position: absolute; left: 405px; top: 540px;
    width: 340px; height: 440px; border-radius: 50%;
    background: var(--watermark);
  }
  .letter {
    position: absolute; left: 63px; top: 292px; width: 552px;
  }
  .salutation { font-size: 18px; font-weight: 400; margin-bottom: 2px; }
  .body-copy {
    font-size: 14.6px; line-height: 20px; text-align: justify;
    color: var(--ink-soft);
  }
  .signature {
    position: absolute; left: 68px; top: 662px;
    width: 155px; height: 46px; border-radius: 4px;
    background: linear-gradient(90deg, var(--signature-tone), #efefef);
  }
  .signatory {
    position: absolute; left: 62px; top: 719px;
    font-size: 11px; color: var(--ink-soft);
  }
  .contact-bar {
    position: absolute; left: 0; top: 795px;
    width: 19px; height: 111px; background: var(--brand-orange);
  }
  .address {
    position: absolute; left: 43px; top: 793px;
    font-size: 12.2px; line-height: 16px; color: var(--ink-soft);
  }
  .contact-list {
    position: absolute; left: 43px; top: 836px; list-style: none;
    font-size: 12.2px; color: var(--ink-soft);
  }
  .contact-list li { display: flex; align-items: center; height: 18.5px; }
  .contact-list svg { width: 10px; height: 10px; margin-right: 6px; fill: var(--brand-orange); }
</style>
</head>
<body>
  <main class="letterhead">
    <div class="watermark" aria-hidden="true"></div>

    <header class="brand">
      <div class="brand-dot" aria-hidden="true"></div>
      <div class="brand-name">DRM SYSTEMS</div>
    </header>

    <section class="letter">
      <p class="salutation">Dear sir,</p>
      <p class="body-copy">Lorem Ipsum. Proin gravida nibh vel velit auctor aliquet. Aenean sollicitudin, lorem quis bibendum auctor, nisi elit consequat ipsum, nec sagittis sem nibh id elit. Duis sed odio sit amet nibh vulputate cursus a sit amet mauris. Morbi accumsan ipsum velit. Nam nec tellus a odio tincidunt auctor a ornare odio. Sed non mauris vitae erat consequat auctor eu in elit. Class aptent taciti sociosqu ad litora torquent per conubia nostra, per inceptos himenaeos. Mauris in erat justo. Nullam ac urna eu felis dapibus condimentum sit amet a augue. Sed non neque elit. Sed ut imperdiet nisi. Proin condimentum fermentum nunc. Etiam pharetra, erat sed fermentum feugiat, velit mauris egestas quam, ut aliquam massa nisl quis neque. Suspendisse in orci enim. Class aptent taciti sociosqu ad litora torquent per conubia nostra, per inceptos himenaeos. Mauris in erat justo. Nullam ac urna eu felis dapibus condimentum sit amet a augue. Sed non neque elit. Sed ut imperdiet nisi. Proin condimentum fermentum nunc. Sed non mauris vitae erat consequat auctor eu in elit. Class aptent taciti sociosqu ad litora torquent per conubia nostra, per inceptos himenaeos. Mauris in erat justo.</p>
    </section>

    <div class="signature" role="img" aria-label="Handwritten signature of Nora Vale"></div>
    <p class="signatory">Nora Vale, Co-Founder &amp; CEO</p>

    <div class="contact-bar" aria-hidden="true"></div>
    <address class="address" style="font-style:normal">Your location address info<br>go in here</address>
    <ul class="contact-list">
      <li><svg viewBox="0 0 10 10" aria-hidden="true"><path d="M1 3c0-1 1-2 4-2s4 1 4 2v1H7V3H3v1H1zM2 5h6l1 4H1z"/></svg>+100 555 0134</li>
      <li><svg viewBox="0 0 10 10" aria-hidden="true"><path d="M2 0h6v3H2zM0 4h10v4H8v2H2V8H0zM3 7v2h4V7z"/></svg>+100 555 0135</li>
      <li><svg viewBox="0 0 10 10" aria-hidden="true"><path d="M0 2h10v6H0zM1 3l4 3 4-3z" fill-rule="evenodd"/></svg>info@drmsystems.com</li>
      <li><svg viewBox="0 0 10 10" aria-hidden="true"><path d="M5 0a5 5 0 1 0 0 10A5 5 0 0 0 5 0zm0 1c.8 0 1.5 1.6 1.6 3.5H3.4C3.5 2.6 4.2 1 5 1zM1.1 4.5h1.3c0-1.2.3-2.2.7-2.9A4 4 0 0 0 1.1 4.5zm0 1a4 4 0 0 0 2 2.9c-.4-.7-.7-1.7-.7-2.9zm2.3 0h3.2C6.5 7.4 5.8 9 5 9s-1.5-1.6-1.6-3.5zm4.2 0c0 1.2-.3 2.2-.7 2.9a4 4 0 0 0 2-2.9zm0-1h1.3a4 4 0 0 0-2-2.9c.4.7.7 1.7.7 2.9z"/></svg>www.drmsystems.com</li>
    </ul>
  </main>
</body>
</html>
```